Website design for Harbor Bolts. ( Lock company)

Harbor Bolts is a New York Based Company that manufactures a variety of high quality Locks which sell worldwide.

Our website: We need a 'face' on the Internet , a website that tells you who we are and what we do - 'An Identity'.

it is not an eCommerce website . the website is to show customers and potential distributers who we are and what we manufacture ( so they come away with a great impression of our company and our products) see www.quarrymillwheel.com

First glance impression: We are Professional; are locks are strong,and reliable. and we are ready to compete with other major Lock companies

Content: for starters the site will contain general information and background about our company (our story), were to buy our products, contact information, and display images of our Locks (and of course all the classic links including to all the legal and technical information). as time goes on we will add more features to the website i.e. Products, Videos blogs etc.

although at first there will not be that much content on the website - it should not look empty (it should be simple and clear but not empty) it should look and feel like a full fledged professional website (not a template)

Inspiration: here are a few sites which have the feel we are looking for:

General tone - quarrymillwheel.com bantrell.com (black is good - But not a must )

Simplicity, clarity - coolvantix.com hearthmate.com

the widescreen Image look - http://www.layoutgarden.com/demo/81952.html

we are considering perhaps having wide HQ images of Lion(s) in the background (but without the felling that it is a zoo or safari website) - it is not a must, its just an idea .

perhaps (if you find it looks good ) use a bit of that metal or chrome look to give it it a strong smooth feel (however it should not look like a dark prison)

We do not currently have a Logo ( if you feel you can design one that fits the above company description - we would love to see if it can work for us) We can talk about additional funds for the logo during this project.

Our working slogan is : Harbor Bolts - "Keeper of the Gate"

for your convenience we have attached a few images of the type of locks we sell

We are looking to collaborate with you throughout the project. We have ideas and visions we want implemented and we will help you along the way. So we can create the perfect website.

Thank you.

```html
<!DOCTYPE html>
<html lang="en">
<head>
<meta charset="utf-8">
<title>Harbor Bolts – Keeper of the Gate</title>
<link href="https://fonts.googleapis.com/css2?family=Oswald:wght@500;700&family=Open+Sans:wght@600;700&family=Roboto+Condensed:wght@400;700&family=Roboto+Slab:wght@700&display=swap" rel="stylesheet">
<style>
:root{
  --red:#ff0033;
  --red-deep:#e4001b;
  --panel:#111111;
  --page:#1c1f1f;
  --navy-top:#0a1a2b;
  --navy-bottom:#06101b;
  --white:#ffffff;
  --body-text:#e8e8e8;
  --muted:#8a8a8a;
  --paper:#f1eadc;
  --rule:#34484a;
  --steel:#b7c2cc;
  --steel-blue:#4a63a8;
  --brass:#d9b255;
  --lockbox:#1d1d1f;
}
*{margin:0;padding:0;box-sizing:border-box}
html,body{width:682px;height:1200px;overflow:hidden;background:var(--page)}
body{position:relative;font-family:"Roboto Condensed",Arial,sans-serif;color:var(--white)}
.abs{position:absolute}

.site-header{left:0;top:0;width:682px;height:85px;background:radial-gradient(ellipse at 50% 0%,#10324a 0%,var(--navy-top) 45%,var(--navy-bottom) 100%);border-bottom:1px solid #1d3142}
.brand{left:0;width:682px;top:9px;text-align:center;font-family:"Open Sans",sans-serif;font-weight:700;font-size:21px;letter-spacing:.3px;color:var(--white)}
.main-nav{left:64px;top:57px;display:flex;list-style:none}
.main-nav li{height:23px;line-height:23px;font-family:"Open Sans",sans-serif;font-size:6.6px;font-weight:600;text-transform:uppercase;text-align:center;color:var(--white)}
.main-nav .active{background:var(--red);width:66px}

.hero{left:0;top:85px;width:682px;height:310px;overflow:hidden;
  background:
    radial-gradient(ellipse 34% 48% at 50% 52%,rgba(70,105,120,.55) 0%,rgba(40,66,80,.35) 55%,rgba(0,0,0,0) 100%),
    radial-gradient(ellipse 60% 75% at 50% 45%,#1e3440 0%,#142530 40%,#0d161c 70%,#0a0d0f 100%)}
.hero-glow{left:255px;top:70px;width:172px;height:230px;border-radius:50%;background:radial-gradient(ellipse,rgba(90,130,150,.25),rgba(0,0,0,0) 70%)}
.hero-mark{left:308px;top:64px;width:62px;height:62px;border:4px solid var(--white);border-radius:50%}
.hero-mark::after{content:"";position:absolute;left:15px;top:17px;width:24px;height:20px;background:var(--red-deep)}
.hero-title{left:0;width:682px;top:138px;text-align:center;font-family:"Oswald",sans-serif;font-weight:700;font-size:33px;line-height:40px;letter-spacing:.5px}
.hero-tagline{left:0;width:682px;top:180px;text-align:center;font-family:"Roboto Slab",serif;font-weight:700;font-size:16px;letter-spacing:.3px}

.content{left:17px;top:395px;width:647px;height:805px;background:linear-gradient(180deg,#121212,#0e0e0e 40%,#101010)}
.section-title{font-family:"Oswald",sans-serif;font-weight:700;font-size:15px;text-transform:uppercase}
.view-all{left:579px;top:415px;font-family:"Open Sans",sans-serif;font-size:7.5px;color:var(--red);text-decoration:underline;font-weight:600}
.lock-thumb{width:116px;height:116px;border-radius:50%;border:2px solid #2d2d2d;box-shadow:0 0 0 1px #444}
.thumb-steel{background:radial-gradient(ellipse 32% 42% at 52% 55%,var(--steel) 0%,#d7dde2 35%,#f6f7f8 60%,#ffffff 100%)}
.thumb-steel-blue{background:radial-gradient(ellipse 36% 38% at 50% 58%,#8fa0c4 0%,#d0d7e4 45%,#f7f8fa 70%,#ffffff 100%)}
.thumb-box{background:radial-gradient(ellipse 22% 38% at 50% 55%,#2a2a2c 0%,#6f6f72 35%,#e9e9ea 65%,#ffffff 100%)}
.thumb-brass{background:radial-gradient(ellipse 36% 28% at 50% 50%,var(--brass) 0%,#ead39a 40%,#faf5e8 70%,#ffffff 100%)}
.carousel-arrow{top:487px}
.divider{left:17px;top:601px;width:647px;height:1px;background:var(--rule)}

.promo{top:623px;width:303px;height:121px;background:linear-gradient(90deg,#ffffff,var(--paper));border:1px solid #ddd}
.promo-image{left:6px;top:5px;width:76px;height:110px;background:radial-gradient(ellipse 45% 50% at 50% 62%,#3a3a3d 0%,var(--lockbox) 55%,#e2ddd2 80%,#f3efe7 100%)}
.promo h3{left:96px;top:17px;font-family:"Oswald",sans-serif;font-weight:700;font-size:14px;line-height:18px;color:var(--red-deep);text-transform:uppercase}
.promo p{left:97px;top:41px;width:196px;font-size:7px;line-height:8.6px;color:#333}
.btn-more{left:96px;top:89px;width:70px;height:20px;background:#1a1a1a;font-family:"Roboto Slab",serif;font-weight:700;font-size:7.5px;line-height:20px;padding-left:7px;color:var(--white)}
.btn-more svg{position:absolute;right:6px;top:5px}

.welcome-title{left:29px;top:762px;font-family:"Oswald",sans-serif;font-weight:700;font-size:19px;line-height:24px}
.welcome-title span{color:var(--red-deep)}
.welcome-copy{left:29px;top:792px;width:377px;font-size:7px;line-height:8.4px;color:var(--body-text)}
.welcome-copy p{margin-bottom:8.4px}
.read-link{left:29px;top:924px;font-size:6.3px;color:var(--red-deep);text-decoration:underline}
.welcome-image{left:411px;top:794px;width:240px;height:129px;
  background:
    radial-gradient(ellipse 18% 40% at 22% 58%,#2a2a2c 0%,#56565a 50%,rgba(255,255,255,0) 100%),
    radial-gradient(ellipse 28% 36% at 68% 52%,var(--brass) 0%,#e6cc8a 45%,rgba(255,255,255,0) 100%),
    #ffffff}

.mailing{left:29px;top:968px;width:622px;height:40px;background:linear-gradient(180deg,#2a2a2a,#151515)}
.mailing .label{left:12px;top:12px;font-size:12px}
.mailing .input{left:133px;top:11px;width:171px;height:18px;background:var(--white);border:2px solid #ccc;font-size:6.5px;color:#222;line-height:14px;padding-left:5px}
.mailing .go{right:0;top:0;width:15px;height:14px;background:#111}
.mailing .touch{left:368px;top:12px;font-size:12px}
.social{top:10px;width:21px;height:21px;border-radius:50%;background:radial-gradient(circle at 35% 30%,#ff4a60,var(--red-deep) 60%,#9c0014);border:1px solid #ffb3bd}

.link-col{top:1022px;width:120px}
.link-col h4{font-size:8px;font-weight:700;margin-bottom:6px}
.link-col ul{list-style:none;padding-left:3px}
.link-col li{font-size:6.8px;line-height:12.8px;color:var(--muted)}
.footer-rule{left:36px;top:1148px;width:610px;height:1px;background:#333}
.legal{left:38px;top:1169px;font-size:6.6px;color:#bbb}
.copyright{right:39px;top:1169px;font-size:6.6px;color:#bbb}
</style>
</head>
<body>

<header class="site-header abs">
  <div class="brand abs">HARBOR BOLTS</div>
  <ul class="main-nav abs">
    <li class="active">Home</li>
    <li style="width:76px">About Us</li>
    <li style="width:75px">Products</li>
    <li style="width:74px">Services</li>
    <li style="width:92px">Testimonials</li>
    <li style="width:78px">Online Shop</li>
    <li style="width:80px">Contact Us</li>
  </ul>
</header>

<section class="hero abs" role="img" aria-label="Dark blue-toned close-up photograph of a lion's head filling the hero banner">
  <div class="hero-glow abs"></div>
  <div class="hero-mark abs"></div>
  <h1 class="hero-title abs">HARBOR BOLTS</h1>
  <div class="hero-tagline abs">KEEPER OF THE GATE</div>
</section>

<main class="content abs"></main>

<h2 class="section-title abs" style="left:29px;top:405px">Explore Locks</h2>
<div class="view-all abs">VIEW ALL LOCKS</div>

<svg class="carousel-arrow abs" style="left:23px" width="16" height="22" viewBox="0 0 16 22"><path d="M13 2 4 11l9 9" fill="none" stroke="#ff0033" stroke-width="4"/></svg>
<div class="lock-thumb thumb-steel abs" style="left:63px;top:439px" role="img" aria-label="Laminated steel padlock with keys"></div>
<div class="lock-thumb thumb-steel-blue abs" style="left:209px;top:439px" role="img" aria-label="Laminated steel padlock with key inserted"></div>
<div class="lock-thumb thumb-box abs" style="left:355px;top:439px" role="img" aria-label="Black combination key lockbox"></div>
<div class="lock-thumb thumb-brass abs" style="left:502px;top:439px" role="img" aria-label="Brass door knob lockset"></div>
<svg class="carousel-arrow abs" style="left:639px" width="16" height="22" viewBox="0 0 16 22"><path d="M3 2l9 9-9 9" fill="none" stroke="#ff0033" stroke-width="4"/></svg>

<div class="divider abs"></div>

<article class="promo abs" style="left:29px">
  <div class="promo-image abs" role="img" aria-label="Black combination key lockbox"></div>
  <h3 class="abs">Lorel Ipsum Dolor Sit Amet</h3>
  <p class="abs">Ut adipiscing urna eu sem auctor, lobortis ultrices ligula pretium. Praesent quis augue ornare, mattis sem nec, aliquet odio. Suspendisse scelerisque condimentum pulvinar. In nec ultricies sapien. Nam volutpat, felis quis condimen.</p>
  <div class="btn-more abs">Read More<svg width="8" height="10" viewBox="0 0 8 10"><path d="M1 1l5 4-5 4" fill="none" stroke="#fff" stroke-width="2"/></svg></div>
</article>
<article class="promo abs" style="left:348px">
  <div class="promo-image abs" role="img" aria-label="Black combination key lockbox"></div>
  <h3 class="abs">Lorel Ipsum Dolor Sit Amet</h3>
  <p class="abs">Ut adipiscing urna eu sem auctor, lobortis ultrices ligula pretium. Praesent quis augue ornare, mattis sem nec, aliquet odio. Suspendisse scelerisque condimentum pulvinar. In nec ultricies sapien. Nam volutpat, felis quis condimen.</p>
  <div class="btn-more abs">Read More<svg width="8" height="10" viewBox="0 0 8 10"><path d="M1 1l5 4-5 4" fill="none" stroke="#fff" stroke-width="2"/></svg></div>
</article>

<h2 class="welcome-title abs">Welcome to <span>Harbor Bolts</span></h2>
<div class="welcome-copy abs">
  <p>Ut adipiscing urna eu sem auctor, lobortis ultrices ligula pretium. Praesent quis augue ornare, mattis sem nec, aliquet odio. Suspendisse scelerisque condimentum pulvinar. In nec ultricies sapien. Nam volutpat, felis quis condimentum ultricies, diam mauris cursus dui, ut molestie nibh ipsum sed ante. Maecenas bibendum tempus augue eu dapibus. Donec ultrices mauris augue, id fringilla velit pharetra et. Donec consectetur turpis nisi, eu dapibus sapien porttitor ut. Etiam gravida lectus sed venenatis tempor. Vivamus ut venenatis diam.</p>
  <p>Cras commodo aliquet justo, sed ultrices nibh vestibulum eget. Nullam euismod tortor id quam pulvinar tincidunt. Donec scelerisque risus vel elit bibendum tincidunt. Fusce quis dapibus purus. Sed metus mi, tempus at augue nec, tincidunt suscipit nisi. Maecenas pretium laoreet nunc. Duis elementum nisl vel nisi iaculis facilisis. In sodales sodales orci auctor accumsan. Ut vestibulum dignissim metus eget laoreet.</p>
  <p>Pellentesque mattis mollis orci ac molestie. Cras dictum tortor a pulvinar vehicula. Proin posuere venenatis odio. Pellentesque nec fermentum diam. Mauris sagittis ut libero ac dignissim. Duis consectetur eleifend tristique. Proin quis ultricies orci. Sed in eros ut mi euismod posuere vitae at magna. Nam at lorem neque. Aenean vel velit est.</p>
</div>
<div class="read-link abs">Red More</div>
<div class="welcome-image abs" role="img" aria-label="Black combination lockbox beside a brass deadbolt lock"></div>

<section class="mailing abs">
  <div class="label abs">Join Our Mailing List</div>
  <div class="input abs">Type your email id
    <div class="go abs"><svg width="15" height="14" viewBox="0 0 15 14"><path d="M5 3l4 4-4 4" fill="none" stroke="#fff" stroke-width="2"/></svg></div>
  </div>
  <div class="touch abs">Get In Touch</div>
  <div class="social abs" style="left:436px"></div>
  <div class="social abs" style="left:466px"></div>
  <div class="social abs" style="left:497px"></div>
  <div class="social abs" style="left:527px"></div>
  <div class="social abs" style="left:557px"></div>
  <div class="social abs" style="left:588px"></div>
</section>

<nav class="link-col abs" style="left:36px"><h4>Quick Link1</h4><ul><li>Home</li><li>About</li><li>Search</li><li>FAQ</li><li>Contact Us</li><li>Store Locator</li></ul></nav>
<nav class="link-col abs" style="left:174px"><h4>Quick Link1</h4><ul><li>Home</li><li>About</li><li>Search</li><li>FAQ</li><li>Contact Us</li><li>Store Locator</li></ul></nav>
<nav class="link-col abs" style="left:312px"><h4>Quick Link1</h4><ul><li>Home</li><li>About</li><li>Search</li><li>FAQ</li><li>Contact Us</li><li>Store Locator</li></ul></nav>
<nav class="link-col abs" style="left:449px"><h4>Quick Link1</h4><ul><li>Home</li><li>About</li><li>Search</li><li>FAQ</li><li>Contact Us</li><li>Store Locator</li></ul></nav>
<nav class="link-col abs" style="left:588px"><h4>Quick Link1</h4><ul><li>Home</li><li>About</li><li>Search</li><li>FAQ</li><li>Contact Us</li><li>Store Locator</li></ul></nav>

<div class="footer-rule abs"></div>
<div class="legal abs">Sitemap &nbsp;&nbsp;|&nbsp;&nbsp; Privacy Policy &nbsp;&nbsp;|&nbsp;&nbsp; Terms of Use</div>
<div class="copyright abs">© 2014, All Rights Reserved</div>

</body>
</html>
```